Speisekarten-Design für Biergarten am Ufer des Bodensees
Super tolle Designerin. Vielen Dank Roswitha!
Zielgruppe
Wir sind ein direkt am Ufer des Bodensees liegender Biergarten, welcher seit über 30 Jahren besteht und deshalb fest in unserer Stadt verwurzelt ist. Zu unserer Zielgruppe gehören Touristen und Einheimische jeglicher Art - wir heißen einfach alle willkommen. Wir bieten unseren Gästen einfache Speisen und lokale Getränke. Uns ist wichtig, dass die Speise- & Getränkekarte das Gefühl von Heimat, Regionalität und Liebe zum Bodensee vermittelt. Wir bevorzugen ein modernes und klares Design, welches jedoch klassische Strukturen wie die eines typischen 60er-Jahre-Diners miteinbezieht.
Aufgabenstellung
Es wäre es toll, wenn diese Faltbar und kompakt (DIN-A4 evtl. etwas größer) ist. Die Textfelder sollten das komplette Speise- und Getränkeangebot darstellen (ca. 15 Gerichte, 6 Biersorten, 6 Softdrinks, 6 Heißgetränke). Wir bevorzugen warme Farbtöne. Es ist nicht notwendig Bilder in der Karte zu hinterlegen.

```html
<!DOCTYPE html>
<html lang="de">
<head>
<meta charset="utf-8">
<title>Speisen &amp; Getränke – Biergarten am Bodensee</title>
<link href="https://fonts.googleapis.com/css2?family=Alegreya+Sans:wght@400;500&family=Alegreya+Sans+SC:wght@700&family=Patrick+Hand&display=swap" rel="stylesheet">
<style>
  :root {
    --stage: #dcdce0;
    --sun-light: #ffe77a;
    --sun-mid: #fdd055;
    --sun-deep: #f6a623;
    --wave: #f4a62a;
    --wave-dark: #e18a1f;
    --ink: #1f1f24;
    --wine: #8c1d12;
    --rule: rgba(150, 90, 20, 0.35);
    --lake: rgba(160, 150, 150, 0.45);
    --body: "Alegreya Sans", sans-serif;
    --caps: "Alegreya Sans SC", sans-serif;
    --hand: "Patrick Hand", cursive;
  }
  * { box-sizing: border-box; margin: 0; padding: 0; }
  html, body { width: 1200px; height: 800px; overflow: hidden; }
  body { background: var(--stage); font-family: var(--body); color: var(--ink); position: relative; }

  .spread {
    position: absolute; top: 30px; width: 540px; height: 740px; overflow: hidden;
    background: linear-gradient(165deg, var(--sun-light) 0%, var(--sun-light) 45%, var(--sun-mid) 75%, var(--sun-deep) 100%);
    box-shadow: 0 6px 18px rgba(0,0,0,0.18);
  }
  .spread--outside { left: 45px; }
  .spread--inside { left: 615px; }
  .waves { position: absolute; inset: 0; width: 100%; height: 100%; }
  .fold { position: absolute; top: 0; bottom: 0; left: 270px; width: 1px; background: rgba(170, 100, 20, 0.35); }
  .panel { position: absolute; top: 0; width: 270px; height: 740px; }
  .panel--left { left: 0; }
  .panel--right { left: 270px; }

  .section-title { position: absolute; font-family: var(--caps); font-weight: 700; font-size: 19px; letter-spacing: 0.5px; color: var(--ink); }

  .menu-list { position: absolute; list-style: none; }
  .menu-item { height: 37px; padding-top: 3px; border-bottom: 1px solid var(--rule); }
  .menu-item:last-child { border-bottom: none; }
  .menu-item__line { display: flex; align-items: baseline; font-size: 13px; }
  .menu-item__no { width: 22px; flex: none; font-size: 11px; }
  .menu-item__name { flex: none; }
  .menu-item__dots { flex: 1; border-bottom: 1.5px dotted var(--ink); margin: 0 2px; transform: translateY(-3px); }
  .menu-item__price { flex: none; }
  .menu-item__detail { padding-left: 22px; font-size: 10px; color: var(--wine); line-height: 1.2; }
  .menu-item__detail sup { font-size: 6px; }

  .lake-map { position: absolute; left: 60px; top: 180px; width: 420px; height: 330px; border-radius: 40% 60% 55% 45% / 30% 40% 60% 70%; background: radial-gradient(ellipse at 55% 55%, var(--lake), rgba(160,150,150,0.15) 70%, transparent 100%); transform: rotate(28deg); }

  .hours { position: absolute; left: 30px; width: 220px; top: 425px; text-align: center; font-size: 11px; line-height: 1.2; }
  .hours__title { font-size: 14px; }
  .hours__note { font-size: 8px; margin-bottom: 12px; }
  .hours__block { margin-bottom: 7px; }
  .hours__block span { opacity: 0.75; }

  .legal { position: absolute; left: 15px; width: 240px; top: 600px; text-align: center; font-size: 5.5px; line-height: 1.35; opacity: 0.8; }
  .legal p { margin-bottom: 5px; }

  .cover-title { position: absolute; left: 20px; top: 55px; width: 240px; text-align: center; font-family: var(--hand); font-size: 56px; line-height: 0.95; color: var(--ink); }
  .cover-tagline { position: absolute; left: 40px; top: 190px; font-family: var(--hand); font-size: 15px; line-height: 1.3; }
  .cover-tagline em { font-style: normal; color: var(--wine); }
  .cover-tagline .indent { padding-left: 70px; display: block; }
  .cover-claims { position: absolute; left: 18px; top: 555px; font-family: var(--hand); font-size: 15px; line-height: 1.45; }
  .cover-claims .indent { padding-left: 30px; }
  .cover-claims .small { font-size: 12px; }
</style>
</head>
<body>

<section class="spread spread--outside" aria-label="Außenseite der Karte">
  <svg class="waves" viewBox="0 0 540 740" preserveAspectRatio="none" aria-hidden="true">
    <path d="M0 0 H540 V30 C440 20 330 10 270 12 C180 15 120 60 60 70 C30 75 10 60 0 40 Z" fill="var(--wave)"/>
    <path d="M20 0 C40 40 90 60 150 40 C190 25 220 15 270 10 V0 Z" fill="var(--wave-dark)" opacity="0.6"/>
    <path d="M0 700 C90 690 180 705 270 720 C360 700 440 690 540 680 V740 H0 Z" fill="var(--wave)"/>
    <path d="M340 740 C360 715 420 700 470 705 C510 710 530 720 540 730 V740 Z" fill="var(--wave-dark)" opacity="0.7"/>
  </svg>
  <div class="fold"></div>

  <div class="lake-map" role="img" aria-label="Umrisskarte des Bodensees als Hintergrundmotiv"></div>

  <div class="panel panel--left">
    <h2 class="section-title" style="left:32px; top:108px;">Heißgetränke</h2>
    <ul class="menu-list" style="left:18px; top:148px; width:215px;">
      <li class="menu-item"><div class="menu-item__line"><span class="menu-item__no">00.</span><span class="menu-item__name">Beispiel Heißgetränke</span><span class="menu-item__dots"></span><span class="menu-item__price">0,00€</span></div><div class="menu-item__detail">Beispieldetail</div></li>
      <li class="menu-item"><div class="menu-item__line"><span class="menu-item__no">00.</span><span class="menu-item__name">Beispiel Heißgetränke</span><span class="menu-item__dots"></span><span class="menu-item__price">0,00€</span></div><div class="menu-item__detail">Beispieldetail</div></li>
      <li class="menu-item"><div class="menu-item__line"><span class="menu-item__no">00.</span><span class="menu-item__name">Beispiel Heißgetränke</span><span class="menu-item__dots"></span><span class="menu-item__price">0,00€</span></div><div class="menu-item__detail">Beispieldetail</div></li>
      <li class="menu-item"><div class="menu-item__line"><span class="menu-item__no">00.</span><span class="menu-item__name">Beispiel Heißgetränke</span><span class="menu-item__dots"></span><span class="menu-item__price">0,00€</span></div><div class="menu-item__detail">Beispieldetail</div></li>
      <li class="menu-item"><div class="menu-item__line"><span class="menu-item__no">00.</span><span class="menu-item__name">Beispiel Heißgetränke</span><span class="menu-item__dots"></span><span class="menu-item__price">0,00€</span></div><div class="menu-item__detail">Beispieldetail</div></li>
      <li class="menu-item"><div class="menu-item__line"><span class="menu-item__no">00.</span><span class="menu-item__name">Beispiel Heißgetränke</span><span class="menu-item__dots"></span><span class="menu-item__price">0,00€</span></div><div class="menu-item__detail">Beispieldetail</div></li>
    </ul>

    <div class="hours">
      <p class="hours__title">Öffnungszeiten</p>
      <p class="hours__note">Mittwoch Ruhetag</p>
      <p class="hours__block">Montag - Samstag<br><span>10:00 - 23:00 Uhr</span></p>
      <p class="hours__block">Montag - Freitag<br><span>zwischen 15:00 - 17:00</span></p>
      <p class="hours__block">Sonntag <span>14:00 - 22:00 Uhr</span><br>an Feiertagen <span>14:00 - 23:00 Uhr</span></p>
    </div>

    <div class="legal">
      <p>Schinken = Vorderschinken<br>1.) Farbstoffe; 2.) Konservierungsstoff; 3.) Nitritpökelsalz und Nitrat; 4.) Antioxidationsmittel;<br>5.) Geschmacksverstärker; 6.) Süßstoffe; 7.) geschwärzt; 10.) Phosphat; 11.) koffeinhaltig<br>*Würstchen = gemischt aus Puten- u. Schweinefleisch</p>
      <p>A1.) Weizenmehl; B.) Krebstiere; C.) Eier; D.) Fisch; E.) Milchprodukte;<br>I.) Sellerie Gewürzmischung; N.) Weichtiere Muscheln, Tintenfisch</p>
      <p>Alle Preise in Euro, Preisänderungen, Druckfehler und Irrtümer vorbehalten<br>Stand Januar 2020 - mit dieser Karte verlieren alle anderen Karten ihre Gültigkeit</p>
    </div>
  </div>

  <div class="panel panel--right">
    <h1 class="cover-title">Speisen &amp;<br>Getränke</h1>
    <p class="cover-tagline">Aus Liebe zum <em>Bodensee</em>,<span class="indent">aus Liebe zur <em>Region</em>.</span></p>
    <div class="cover-claims">
      <p>Original &amp; Regional</p>
      <p>Heimat des guten geschmacks</p>
      <p>Das Herz, die Seele &amp;</p>
      <p class="indent">der Geschmack des Bodensees</p>
      <p class="small">Aus Liebe zum Bodensee, aus Liebe zur Region</p>
    </div>
  </div>
</section>

<section class="spread spread--inside" aria-label="Innenseite der Karte">
  <svg class="waves" viewBox="0 0 540 740" preserveAspectRatio="none" aria-hidden="true">
    <path d="M0 0 H540 V50 C460 40 360 30 270 30 C180 30 90 25 0 20 Z" fill="var(--wave)"/>
    <path d="M300 30 C360 28 420 15 470 5 C450 60 400 80 360 75 C320 70 300 55 300 30 Z" fill="var(--wave-dark)" opacity="0.6"/>
    <path d="M270 30 C330 40 420 60 480 50 C510 40 530 20 540 0 V60 C500 70 400 70 270 55 Z" fill="var(--wave)" opacity="0.5"/>
    <path d="M0 720 C40 660 110 650 160 655 C200 660 240 665 270 668 C360 670 450 680 540 690 V740 H0 Z" fill="var(--wave)"/>
    <path d="M90 740 C110 715 150 705 200 705 C250 705 260 715 270 720 V740 Z" fill="var(--wave-dark)" opacity="0.6"/>
  </svg>
  <div class="fold"></div>

  <div class="panel panel--left">
    <h2 class="section-title" style="left:34px; top:65px;">Gerichte</h2>
    <ul class="menu-list" style="left:18px; top:100px; width:225px;">
      <li class="menu-item"><div class="menu-item__line"><span class="menu-item__no">00.</span><span class="menu-item__name">Beispiel Gericht</span><span class="menu-item__dots"></span><span class="menu-item__price">0,00€</span></div><div class="menu-item__detail">Schinken<sup>2,5,10</sup>, Gouda<sup>G</sup> und Salami</div></li>
      <li class="menu-item"><div class="menu-item__line"><span class="menu-item__no">00.</span><span class="menu-item__name">Beispiel Gericht</span><span class="menu-item__dots"></span><span class="menu-item__price">0,00€</span></div><div class="menu-item__detail">Schinken<sup>2,5,10</sup>, Gouda<sup>G</sup> und Salami</div></li>
      <li class="menu-item"><div class="menu-item__line"><span class="menu-item__no">00.</span><span class="menu-item__name">Beispiel Gericht</span><span class="menu-item__dots"></span><span class="menu-item__price">0,00€</span></div><div class="menu-item__detail">Schinken<sup>2,5,10</sup>, Gouda<sup>G</sup> und Salami</div></li>
      <li class="menu-item"><div class="menu-item__line"><span class="menu-item__no">00.</span><span class="menu-item__name">Beispiel Gericht</span><span class="menu-item__dots"></span><span class="menu-item__price">0,00€</span></div><div class="menu-item__detail">Schinken<sup>2,5,10</sup>, Gouda<sup>G</sup> und Salami</div></li>
      <li class="menu-item"><div class="menu-item__line"><span class="menu-item__no">00.</span><span class="menu-item__name">Beispiel Gericht</span><span class="menu-item__dots"></span><span class="menu-item__price">0,00€</span></div><div class="menu-item__detail">Schinken<sup>2,5,10</sup>, Gouda<sup>G</sup> und Salami</div></li>
      <li class="menu-item"><div class="menu-item__line"><span class="menu-item__no">00.</span><span class="menu-item__name">Beispiel Gericht</span><span class="menu-item__dots"></span><span class="menu-item__price">0,00€</span></div><div class="menu-item__detail">Schinken<sup>2,5,10</sup>, Gouda<sup>G</sup> und Salami</div></li>
      <li class="menu-item"><div class="menu-item__line"><span class="menu-item__no">00.</span><span class="menu-item__name">Beispiel Gericht</span><span class="menu-item__dots"></span><span class="menu-item__price">0,00€</span></div><div class="menu-item__detail">Schinken<sup>2,5,10</sup>, Gouda<sup>G</sup> und Salami</div></li>
      <li class="menu-item"><div class="menu-item__line"><span class="menu-item__no">00.</span><span class="menu-item__name">Beispiel Gericht</span><span class="menu-item__dots"></span><span class="menu-item__price">0,00€</span></div><div class="menu-item__detail">Schinken<sup>2,5,10</sup>, Gouda<sup>G</sup> und Salami</div></li>
      <li class="menu-item"><div class="menu-item__line"><span class="menu-item__no">00.</span><span class="menu-item__name">Beispiel Gericht</span><span class="menu-item__dots"></span><span class="menu-item__price">0,00€</span></div><div class="menu-item__detail">Schinken<sup>2,5,10</sup>, Gouda<sup>G</sup> und Salami</div></li>
      <li class="menu-item"><div class="menu-item__line"><span class="menu-item__no">00.</span><span class="menu-item__name">Beispiel Gericht</span><span class="menu-item__dots"></span><span class="menu-item__price">0,00€</span></div><div class="menu-item__detail">Schinken<sup>2,5,10</sup>, Gouda<sup>G</sup> und Salami</div></li>
      <li class="menu-item"><div class="menu-item__line"><span class="menu-item__no">00.</span><span class="menu-item__name">Beispiel Gericht</span><span class="menu-item__dots"></span><span class="menu-item__price">0,00€</span></div><div class="menu-item__detail">Schinken<sup>2,5,10</sup>, Gouda<sup>G</sup> und Salami</div></li>
      <li class="menu-item"><div class="menu-item__line"><span class="menu-item__no">00.</span><span class="menu-item__name">Beispiel Gericht</span><span class="menu-item__dots"></span><span class="menu-item__price">0,00€</span></div><div class="menu-item__detail">Schinken<sup>2,5,10</sup>, Gouda<sup>G</sup> und Salami</div></li>
      <li class="menu-item"><div class="menu-item__line"><span class="menu-item__no">00.</span><span class="menu-item__name">Beispiel Gericht</span><span class="menu-item__dots"></span><span class="menu-item__price">0,00€</span></div><div class="menu-item__detail">Schinken<sup>2,5,10</sup>, Gouda<sup>G</sup> und Salami</div></li>
      <li class="menu-item"><div class="menu-item__line"><span class="menu-item__no">00.</span><span class="menu-item__name">Beispiel Gericht</span><span class="menu-item__dots"></span><span class="menu-item__price">0,00€</span></div><div class="menu-item__detail">Schinken<sup>2,5,10</sup>, Gouda<sup>G</sup> und Salami</div></li>
      <li class="menu-item"><div class="menu-item__line"><span class="menu-item__no">00.</span><span class="menu-item__name">Beispiel Gericht</span><span class="menu-item__dots"></span><span class="menu-item__price">0,00€</span></div><div class="menu-item__detail">Schinken<sup>2,5,10</sup>, Gouda<sup>G</sup> und Salami</div></li>
    </ul>
  </div>

  <div class="panel panel--right">
    <h2 class="section-title" style="right:30px; top:112px;">Biere</h2>
    <ul class="menu-list" style="left:18px; top:150px; width:225px;">
      <li class="menu-item"><div class="menu-item__line"><span class="menu-item__no">00.</span><span class="menu-item__name">Beispiel Bier</span><span class="menu-item__dots"></span><span class="menu-item__price">0,00€</span></div><div class="menu-item__detail">Beispieldetail</div></li>
      <li class="menu-item"><div class="menu-item__line"><span class="menu-item__no">00.</span><span class="menu-item__name">Beispiel Bier</span><span class="menu-item__dots"></span><span class="menu-item__price">0,00€</span></div><div class="menu-item__detail">Beispieldetail</div></li>
      <li class="menu-item"><div class="menu-item__line"><span class="menu-item__no">00.</span><span class="menu-item__name">Beispiel Bier</span><span class="menu-item__dots"></span><span class="menu-item__price">0,00€</span></div><div class="menu-item__detail">Beispieldetail</div></li>
      <li class="menu-item"><div class="menu-item__line"><span class="menu-item__no">00.</span><span class="menu-item__name">Beispiel Bier</span><span class="menu-item__dots"></span><span class="menu-item__price">0,00€</span></div><div class="menu-item__detail">Beispieldetail</div></li>
      <li class="menu-item"><div class="menu-item__line"><span class="menu-item__no">00.</span><span class="menu-item__name">Beispiel Bier</span><span class="menu-item__dots"></span><span class="menu-item__price">0,00€</span></div><div class="menu-item__detail">Beispieldetail</div></li>
      <li class="menu-item"><div class="menu-item__line"><span class="menu-item__no">00.</span><span class="menu-item__name">Beispiel Bier</span><span class="menu-item__dots"></span><span class="menu-item__price">0,00€</span></div><div class="menu-item__detail">Beispieldetail</div></li>
    </ul>

    <h2 class="section-title" style="right:30px; top:425px;">Softdrinks</h2>
    <ul class="menu-list" style="left:18px; top:470px; width:225px;">
      <li class="menu-item"><div class="menu-item__line"><span class="menu-item__no">00.</span><span class="menu-item__name">Beispiel Softdrink</span><span class="menu-item__dots"></span><span class="menu-item__price">0,00€</span></div><div class="menu-item__detail">Beispieldetail</div></li>
      <li class="menu-item"><div class="menu-item__line"><span class="menu-item__no">00.</span><span class="menu-item__name">Beispiel Softdrink</span><span class="menu-item__dots"></span><span class="menu-item__price">0,00€</span></div><div class="menu-item__detail">Beispieldetail</div></li>
      <li class="menu-item"><div class="menu-item__line"><span class="menu-item__no">00.</span><span class="menu-item__name">Beispiel Softdrink</span><span class="menu-item__dots"></span><span class="menu-item__price">0,00€</span></div><div class="menu-item__detail">Beispieldetail</div></li>
      <li class="menu-item"><div class="menu-item__line"><span class="menu-item__no">00.</span><span class="menu-item__name">Beispiel Softdrink</span><span class="menu-item__dots"></span><span class="menu-item__price">0,00€</span></div><div class="menu-item__detail">Beispieldetail</div></li>
      <li class="menu-item"><div class="menu-item__line"><span class="menu-item__no">00.</span><span class="menu-item__name">Beispiel Softdrink</span><span class="menu-item__dots"></span><span class="menu-item__price">0,00€</span></div><div class="menu-item__detail">Beispieldetail</div></li>
      <li class="menu-item"><div class="menu-item__line"><span class="menu-item__no">00.</span><span class="menu-item__name">Beispiel Softdrink</span><span class="menu-item__dots"></span><span class="menu-item__price">0,00€</span></div><div class="menu-item__detail">Beispieldetail</div></li>
    </ul>
  </div>
</section>

</body>
</html>
```